3-4 Page Research Report Template

We want a template in MS Word that we can use to write up research reports. We want a similar feal as our newsletter and website - but we also want it to look more modern, yet stay in the financial service / investment research world.

Examples: http://media.brelvox.example/Documents/Asset_Allocation_Focus_March2013.pdf

http://www.taskirel.example/Home/Documents/Default.aspx?fileId=58082

Our website: www.hurmontadvisors.example
Our Newsletter: http://www.hurmontadvisors.example/DawlinBrief/2012/2012-11-12.pdf

We want 3 template pages - a cover or 1st page, a middle page and and last or end page.

Reason: I would like more than two designers to compare ideas. I was hoping for 5. This is designers not designs.

We are not looking for a new version of our Newsletter "The Dawlin Brief" - We want a template to publish other research articles. We shared The Dawlin Brief file to give you a better idea on what we currently like / use - though dated as it was designed in 2004. 

That doesn't mean we wont pick a template using The Dawlin Brief as example content. I just wanted to be clear. 

Target Market(s)

Sophisticated investors with over $1M in the market and investment professionals (financial advisors)

Industry/Entity Type

Investment

Requirements
Must have
• Space for disclosures at the end.
Ability to drop in tables and charts/graphs
Should not have
• Do not use the HMRA website masthead directly. Please be creative in helping is get a more modern and fresh design. I provided it as reference on what we already like (or did in 2004 when it was designed).

```html
<!DOCTYPE html>
<html lang="en">
<head>
<meta charset="utf-8">
<title>Research Report — Cover Page</title>
<link rel="stylesheet" href="https://fonts.googleapis.com/css2?family=Source+Sans+3:wght@400;700&display=swap">
<style>
  :root {
    --brand-blue: #0d4f94;
    --warm-gray: #8a8782;
    --paper: #ffffff;
  }
  html, body {
    margin: 0;
    padding: 0;
    overflow: hidden;
    background: var(--paper);
  }
  .cover-page {
    position: relative;
    width: 848px;
    height: 1200px;
    overflow: hidden;
    background: var(--paper);
    font-family: "Source Sans 3", "Myriad Pro", Arial, sans-serif;
  }
  .masthead-band {
    position: absolute;
    left: 41px;
    top: 54px;
    width: 767px;
    height: 77px;
    background: linear-gradient(90deg, #0b4a8e 0%, #0f5399 60%, #0d4f94 100%);
  }
  .brand-mark {
    position: absolute;
    left: 600px;
    top: 200px;
    width: 208px;
    display: flex;
    align-items: center;
    justify-content: flex-end;
    gap: 10px;
  }
  .brand-mark__dot {
    width: 22px;
    height: 22px;
    border-radius: 50%;
    background: var(--warm-gray);
    flex: none;
  }
  .brand-mark__name {
    margin: 0;
    font-size: 22px;
    font-weight: 700;
    color: var(--brand-blue);
    white-space: nowrap;
  }
  .report-title {
    position: absolute;
    left: 41px;
    top: 364px;
    margin: 0;
    font-size: 30px;
    font-weight: 700;
    letter-spacing: -0.2px;
    color: var(--brand-blue);
  }
  .report-summary {
    position: absolute;
    left: 41px;
    top: 427px;
    width: 770px;
    margin: 0;
    font-size: 17.4px;
    line-height: 24.5px;
    font-weight: 700;
    color: var(--warm-gray);
  }
  .cover-chart {
    position: absolute;
    left: 0;
    top: 0;
  }
  .cover-chart .bar {
    fill: var(--warm-gray);
  }
</style>
</head>
<body>
  <main class="cover-page">
    <div class="masthead-band" role="img" aria-label="Blue header band with flowing thin white wave lines"></div>

    <div class="brand-mark">
      <span class="brand-mark__dot"></span>
      <p class="brand-mark__name">Hurmont Advisors</p>
    </div>

    <h1 class="report-title">Lorem ipsum dolor sit amet</h1>
    <p class="report-summary">Morbi euismod sem eget neque consectetur a ultrices nunc porta. Pellentesque pharetra, lacus pharetra vehicula consequat, neque est luctus mauris, at lobortis mauris elit ac felis. Vestibulum blandit nulla at massa lacinia suscipit.</p>

    <svg class="cover-chart" width="848" height="1200" viewBox="0 0 848 1200" aria-hidden="true">
      <rect class="bar" x="41"  y="591" width="81" height="575"/>
      <rect class="bar" x="139" y="704" width="81" height="462"/>
      <rect class="bar" x="237" y="838" width="81" height="328"/>
      <rect class="bar" x="335" y="734" width="81" height="432"/>
      <rect class="bar" x="433" y="815" width="81" height="351"/>
      <rect class="bar" x="531" y="758" width="81" height="408"/>
      <rect class="bar" x="629" y="704" width="81" height="462"/>
      <rect class="bar" x="727" y="567" width="81" height="599"/>
    </svg>
  </main>
</body>
</html>
```